Wageline Associates Business Card Design

We need a business card designed around our new logo. The business card should be modern in design & should communicate success, confidence, power, sophistication. The target market is young business professionals. This is for a human resource & payroll outsourcing business.

```html
<!DOCTYPE html>
<html lang="en">
<head>
<meta charset="utf-8">
<title>Wageline Associates Business Card</title>
<link rel="stylesheet" href="https://fonts.googleapis.com/css2?family=Montserrat:wght@400;500;600;700&display=swap">
<style>
  :root {
    --backdrop: #2a2b2f;
    --card-white: #ffffff;
    --ink: #111113;
    --ink-soft: #2b2b2b;
    --band-black: #0c0c0d;
    --accent-red: #e8222b;
    --accent-red-deep: #c8202a;
    --muted: #bdbdbd;
  }
  * { box-sizing: border-box; margin: 0; padding: 0; }
  html, body {
    width: 1200px; height: 900px; overflow: hidden;
    background: var(--backdrop);
    font-family: "Montserrat", Arial, sans-serif;
  }
  .card {
    position: absolute; left: 100px; top: 164px;
    width: 1000px; height: 572px;
    background: var(--card-white);
    border-radius: 36px;
    overflow: hidden;
    box-shadow: 0 20px 50px rgba(0,0,0,0.45);
  }
  .card__base { position: absolute; inset: 0; width: 100%; height: 100%; }
  .brand {
    position: absolute; left: 400px; top: 52px;
    display: flex; align-items: center; gap: 14px;
  }
  .brand__dot { width: 22px; height: 22px; border-radius: 50%; background: var(--accent-red); }
  .brand__name {
    font-size: 34px; font-weight: 600; color: var(--ink);
    letter-spacing: 0.5px;
  }
  .name-band {
    position: absolute; left: 0; top: 150px;
    width: 590px; height: 110px;
    background: var(--band-black);
    border-radius: 0 55px 55px 0;
  }
  .name-band__role {
    position: absolute; left: 170px; top: 16px;
    font-size: 18px; font-weight: 400; color: var(--muted);
  }
  .name-band__name {
    position: absolute; left: 170px; top: 44px;
    font-size: 34px; font-weight: 700; color: var(--card-white);
    letter-spacing: 1px;
  }
  .name-band__dot {
    position: absolute; right: 34px; top: 38px;
    width: 34px; height: 34px; border-radius: 50%;
    background: var(--accent-red);
  }
  .contacts {
    position: absolute; left: 52px; top: 290px;
    list-style: none; display: flex; flex-direction: column; gap: 14px;
  }
  .contacts__item {
    display: flex; align-items: center; gap: 16px;
    font-size: 21px; font-weight: 500; color: var(--ink-soft);
  }
  .contacts__icon { width: 30px; height: 30px; flex: none; }
</style>
</head>
<body>
  <main class="card" aria-label="Business card front">
    <svg class="card__base" viewBox="0 0 1000 572" preserveAspectRatio="none" aria-hidden="true">
      <path fill="var(--accent-red)" d="M0,462 C380,452 720,330 1000,108 L1000,162 C720,390 380,500 0,508 Z"/>
      <path fill="var(--band-black)" d="M0,500 C380,492 720,384 1000,156 L1000,572 L0,572 Z"/>
    </svg>

    <div class="brand">
      <span class="brand__dot"></span>
      <span class="brand__name">Wageline Associates</span>
    </div>

    <div class="name-band">
      <p class="name-band__role">Director</p>
      <h1 class="name-band__name">MARCUS HALE</h1>
      <span class="name-band__dot"></span>
    </div>

    <ul class="contacts">
      <li class="contacts__item">
        <svg class="contacts__icon" viewBox="0 0 30 30" aria-hidden="true">
          <circle cx="15" cy="15" r="15" fill="var(--accent-red)"/>
          <path fill="#fff" d="M10 8 l3 0 l1.5 4 l-2 1.5 c1 2 2.5 3.5 4.5 4.5 l1.5 -2 l4 1.5 l0 3 c0 1 -1 1.5 -2 1.5 c-6 -0.5 -11 -5.5 -11.5 -11.5 c0 -1 0.5 -2 1 -2.5 z"/>
        </svg>
        <span>+12 98 76 543</span>
      </li>
      <li class="contacts__item">
        <svg class="contacts__icon" viewBox="0 0 30 30" aria-hidden="true">
          <circle cx="15" cy="15" r="15" fill="var(--accent-red)"/>
          <rect x="8" y="10" width="14" height="10" rx="1" fill="#fff"/>
          <path d="M8 10.5 L15 16 L22 10.5" fill="none" stroke="var(--accent-red)" stroke-width="1.5"/>
        </svg>
        <span>hello@wagelineassociates.com</span>
      </li>
      <li class="contacts__item">
        <svg class="contacts__icon" viewBox="0 0 30 30" aria-hidden="true">
          <circle cx="15" cy="15" r="15" fill="var(--accent-red)"/>
          <g fill="none" stroke="#fff" stroke-width="1.6">
            <circle cx="15" cy="15" r="7"/>
            <ellipse cx="15" cy="15" rx="3" ry="7"/>
            <path d="M8 15 H22 M9.5 11 H20.5 M9.5 19 H20.5"/>
          </g>
        </svg>
        <span>wagelineassociates.com</span>
      </li>
    </ul>
  </main>
</body>
</html>
```